business card design for luxurious real estate brand

using the attached logo, i am looking for a 2-sided business card design. the back should be the gold logo on black background. the front needs to include: gold logo, name, phone, email, and website

Industry/Entity Type

real estate

Contact Information for Business Card

logo, name, email, phone, website

Font styles to use
Sans Serif

```html
<!DOCTYPE html>
<html lang="en">
<head>
<meta charset="UTF-8">
<title>Villa Serrano – Business Card</title>
<link rel="stylesheet" href="https://fonts.googleapis.com/css2?family=Montserrat:wght@300;400;500;700&display=swap">
<style>
  :root {
    --backdrop: #979797;
    --card: #111111;
    --gold: #ffcc00;
    --white: #ffffff;
    --muted: #7a7a7a;
    --rule: #555555;
  }
  * { margin: 0; padding: 0; box-sizing: border-box; }
  html, body { width: 1200px; height: 1000px; overflow: hidden; }
  body {
    background: var(--backdrop);
    font-family: "Montserrat", sans-serif;
    position: relative;
  }
  .card {
    position: absolute;
    left: 293px;
    width: 614px;
    height: 350px;
    background: var(--card);
    border-radius: 32px;
  }
  .card--brand { top: 100px; }
  .card--contact { top: 511px; }

  .brand-name {
    position: absolute;
    color: var(--gold);
    font-weight: 500;
    white-space: nowrap;
    display: flex;
    align-items: center;
  }
  .brand-name__mark {
    display: inline-block;
    background: var(--gold);
  }
  .card--brand .brand-name {
    left: 0; right: 0; top: 150px;
    justify-content: center;
    font-size: 32px;
    letter-spacing: 5px;
    gap: 18px;
  }
  .card--brand .brand-name__mark { width: 22px; height: 22px; }

  .card--contact .brand-name {
    left: 86px; top: 162px;
    font-size: 16px;
    letter-spacing: 3px;
    gap: 10px;
  }
  .card--contact .brand-name__mark { width: 11px; height: 11px; }

  .divider {
    position: absolute;
    left: 306px; top: 108px;
    width: 2px; height: 135px;
    background: var(--rule);
  }
  .person {
    position: absolute;
    left: 339px; top: 106px;
  }
  .person__name {
    color: var(--white);
    font-weight: 700;
    font-size: 15px;
    letter-spacing: 3px;
    line-height: 18px;
  }
  .person__role {
    color: var(--muted);
    font-weight: 300;
    font-size: 15px;
    letter-spacing: 3.2px;
    line-height: 22px;
  }
  .contacts {
    position: absolute;
    left: 339px; top: 172px;
    list-style: none;
  }
  .contacts li {
    display: flex;
    align-items: center;
    height: 22.5px;
    color: var(--white);
    font-size: 15.5px;
  }
  .contacts svg {
    width: 15px; height: 15px;
    margin-right: 9px;
    fill: none;
    stroke: var(--gold);
  }
</style>
</head>
<body>
  <section class="card card--brand">
    <div class="brand-name"><span class="brand-name__mark"></span>VILLA SERRANO</div>
  </section>

  <section class="card card--contact">
    <div class="brand-name"><span class="brand-name__mark"></span>VILLA SERRANO</div>
    <div class="divider"></div>
    <div class="person">
      <p class="person__name">NAME SURNAME</p>
      <p class="person__role">POSITION</p>
    </div>
    <ul class="contacts">
      <li>
        <svg viewBox="0 0 15 15" aria-hidden="true"><rect x="3.5" y="0.8" width="8" height="13.4" rx="1.2" stroke-width="1.6"/><line x1="6.5" y1="11.5" x2="8.5" y2="11.5" stroke-width="1.4"/></svg>
        012 345 6789
      </li>
      <li>
        <svg viewBox="0 0 15 15" aria-hidden="true"><rect x="0.8" y="3" width="13.4" height="9.5" fill="#ffcc00" stroke="none"/><polyline points="1,3.5 7.5,8.5 14,3.5" stroke="#111" stroke-width="1.3"/></svg>
        email@villaserrano.com
      </li>
      <li>
        <svg viewBox="0 0 15 15" aria-hidden="true" stroke-width="1.3"><circle cx="7.5" cy="7.5" r="6.3"/><ellipse cx="7.5" cy="7.5" rx="2.8" ry="6.3"/><line x1="1.2" y1="7.5" x2="13.8" y2="7.5"/><line x1="2.3" y1="4.3" x2="12.7" y2="4.3"/><line x1="2.3" y1="10.7" x2="12.7" y2="10.7"/></svg>
        www.villaserrano.com
      </li>
    </ul>
  </section>
</body>
</html>
```